Climbing the Crestward Ridge: Outcome-Led Lean Renewal

Target is Halvorsen 100 managers in Information Technology. I've led Agile transformations for over 60 organizations since 2005. One of these organizations is using my collateral internally so I'm branding and copyrighting key concepts. I've attached a rough idea of what I'm looking for. My website is www.outcomeledlean-demo.com.

```html
<!DOCTYPE html>
<html lang="en">
<head>
<meta charset="utf-8">
<title>Climbing the Crestward Ridge</title>
<link rel="stylesheet" href="https://fonts.googleapis.com/css2?family=Carlito:wght@400;700&display=swap">
<style>
  :root {
    --ink: #000000;
    --paper: #ffffff;
    --banner: #f9bf2e;
    --ray: #fcd460;
    --performance: #f5a342;
    --performance-fold: #7a4f1e;
    --practices: #e9795a;
    --practices-fold: #7a3a27;
    --principles: #56bec4;
    --principles-fold: #2b6468;
    --people: #48a3d9;
    --people-fold: #235675;
    --processes: #8a85ab;
    --rule: #e9795a;
    --heart: #f21d1d;
    --board: #dcdcdc;
    --board-edge: #8a8a8a;
    --cycle-area: #e6e6e6;
  }
  html, body {
    margin: 0;
    padding: 0;
    width: 1200px;
    height: 675px;
    overflow: hidden;
    background: var(--paper);
  }
  .canvas {
    display: block;
    width: 1200px;
    height: 675px;
    font-family: "Carlito", "Calibri", sans-serif;
  }
  .title { font-size: 68px; font-weight: 700; fill: var(--ink); }
  .banner-label { font-size: 38px; font-weight: 700; fill: var(--ink); }
  .tier-label { font-size: 23px; fill: var(--ink); }
  .concept { font-size: 68px; font-weight: 700; fill: var(--ink); }
  .footer { font-size: 24px; fill: var(--ink); }
  .icon { fill: none; stroke: var(--ink); stroke-width: 4; stroke-linecap: round; stroke-linejoin: round; }
  .icon-solid { fill: var(--ink); }
  .rule { stroke: var(--rule); stroke-width: 1.5; }
</style>
</head>
<body>
<svg class="canvas" viewBox="0 0 1500 844" xmlns="http://www.w3.org/2000/svg">
  <defs>
    <linearGradient id="rayFade" x1="0" y1="0" x2="0" y2="1">
      <stop offset="0" stop-color="var(--ray)" stop-opacity="0.95"/>
      <stop offset="1" stop-color="var(--ray)" stop-opacity="0"/>
    </linearGradient>
  </defs>

  <text class="title" x="750" y="84" text-anchor="middle">Climbing the Crestward Ridge</text>

  <!-- light rays -->
  <g class="rays" fill="url(#rayFade)">
    <polygon points="520,160 560,160 750,215"/>
    <polygon points="590,160 625,160 750,215"/>
    <polygon points="655,160 685,160 750,215"/>
    <polygon points="715,160 740,160 750,215"/>
    <polygon points="760,160 785,160 750,215"/>
    <polygon points="815,160 845,160 750,215"/>
    <polygon points="875,160 910,160 750,215"/>
    <polygon points="940,160 980,160 750,215"/>
    <polygon points="990,175 1000,190 750,215"/>
    <polygon points="500,175 510,190 750,215"/>
  </g>

  <!-- banner -->
  <polygon class="banner" fill="var(--banner)" points="420,108 1080,108 1110,137 1080,166 420,166 390,137"/>
  <text class="banner-label" x="750" y="150" text-anchor="middle">Workforce Transformation</text>

  <!-- pyramid tiers -->
  <g class="tier tier-performance">
    <polygon fill="var(--performance-fold)" points="683,277 738,277 712,296"/>
    <polygon fill="var(--performance)" points="750,195 820,277 680,277"/>
    <g class="icon">
      <path d="M718 262 Q750 228 782 262"/>
      <path d="M726 262 Q750 240 774 262"/>
      <line x1="716" y1="265" x2="784" y2="265"/>
    </g>
    <g class="icon-solid">
      <circle cx="750" cy="232" r="5"/>
      <circle cx="728" cy="244" r="4"/>
      <circle cx="772" cy="244" r="4"/>
    </g>
    <line class="rule" x1="812" y1="248" x2="978" y2="248"/>
    <text class="tier-label" x="978" y="240" text-anchor="end">Performance</text>
  </g>

  <g class="tier tier-practices">
    <polygon fill="var(--practices-fold)" points="614,366 670,366 640,385"/>
    <polygon fill="var(--practices)" points="657,294 836,294 887,366 612,366"/>
    <g class="icon">
      <circle cx="745" cy="332" r="22"/>
      <circle cx="745" cy="332" r="12"/>
      <line x1="745" y1="332" x2="776" y2="304"/>
    </g>
    <polygon class="icon-solid" points="776,298 784,300 782,310 772,308"/>
    <line class="rule" x1="860" y1="333" x2="978" y2="333"/>
    <text class="tier-label" x="978" y="326" text-anchor="end">Practices</text>
  </g>

  <g class="tier tier-principles">
    <polygon fill="var(--principles-fold)" points="547,457 602,457 574,476"/>
    <polygon fill="var(--principles)" points="590,385 903,385 955,457 545,457"/>
    <g class="icon">
      <rect x="720" y="398" width="36" height="46" rx="3"/>
      <line x1="728" y1="410" x2="746" y2="410"/>
      <line x1="728" y1="420" x2="742" y2="420"/>
      <circle cx="758" cy="428" r="12"/>
      <line x1="758" y1="428" x2="778" y2="410"/>
    </g>
    <text class="tier-label" x="813" y="428">Principles</text>
  </g>

  <g class="tier tier-people">
    <polygon fill="var(--people-fold)" points="479,547 534,547 506,566"/>
    <polygon fill="var(--people)" points="522,475 980,475 1025,547 477,547"/>
    <g class="icon-solid">
      <circle cx="750" cy="490" r="7"/>
      <rect x="741" y="499" width="18" height="36" rx="4"/>
      <circle cx="733" cy="494" r="5"/>
      <rect x="727" y="501" width="12" height="28" rx="3"/>
      <circle cx="767" cy="494" r="5"/>
      <rect x="761" y="501" width="12" height="28" rx="3"/>
      <circle cx="721" cy="499" r="4"/>
      <rect x="716" y="505" width="9" height="20" rx="3"/>
      <circle cx="779" cy="499" r="4"/>
      <rect x="775" y="505" width="9" height="20" rx="3"/>
    </g>
    <text class="tier-label" x="984" y="519" text-anchor="end">People</text>
  </g>

  <g class="tier tier-processes">
    <polygon fill="var(--processes)" points="457,566 1042,566 1093,638 408,638"/>
    <g class="icon">
      <path d="M726 590 A28 28 0 0 1 774 594"/>
      <path d="M774 614 A28 28 0 0 1 726 610"/>
      <circle cx="750" cy="602" r="10"/>
      <path d="M750 584 V589 M750 615 V620 M732 602 H737 M763 602 H768 M737 589 L741 593 M759 611 L763 615 M763 589 L759 593 M737 615 L741 611"/>
    </g>
    <text class="tier-label" x="1051" y="615" text-anchor="end">Processes</text>
  </g>

  <!-- kanban -->
  <g class="concept-kanban">
    <rect x="277" y="353" width="137" height="113" rx="4" fill="var(--board)" stroke="var(--board-edge)" stroke-width="2" role="img" aria-label="Kanban board with columns of coloured task cards"/>
    <text class="concept" x="344" y="430" text-anchor="middle">kanban</text>
  </g>

  <!-- kaizen -->
  <g class="concept-kaizen">
    <circle cx="1228" cy="410" r="62" fill="var(--cycle-area)" role="img" aria-label="Continuous-improvement cycle graphic"/>
    <text class="concept" x="1228" y="430" text-anchor="middle">kaizen</text>
  </g>

  <!-- kokoro -->
  <g class="concept-kokoro">
    <path fill="var(--heart)" d="M750 768 C720 740 645 712 645 690 C645 664 660 651 695 651 C725 651 745 668 750 680 C755 668 775 651 805 651 C840 651 855 664 855 690 C855 712 780 740 750 768 Z"/>
    <text class="concept" x="750" y="725" text-anchor="middle">kokoro</text>
  </g>

  <text class="footer" x="750" y="813" text-anchor="middle">© 2018 Outcome-Led Lean | OutcomeLedLean-demo.com</text>
</svg>
</body>
</html>
```